Redesign of Grantlyhub.com

We need a redesign of some key-pages on our crowdfunding website for mobile apps, GrantlyHub.com.

- Redesign of homepage
http://www.grantlyhub.com/en

- Redesign of project submission page
http://www.grantlyhub.com/en/submit-your-app/submit-your-app

- Redesign of browsing section
http://www.grantlyhub.com/en/fund-apps

- Redesign of project funding page
http://www.grantlyhub.com/en/fund-apps/sponsor/sketch-riddler?amount=5.00

Design should be highly focused on a great user experience for users of the platform, being in principal mobile developers. So we need a great user experience for mobile developers using our service.

Benchmark designs we particularly like are:
http://www.pledgorama.com/
http://www.tradebitly.com/landing/
http://www.vomba.com/

Design should have a more 'fun, happy to get involved' factor as it has nox.
Updates

Logo's have been uploaded

Target Market(s)

mobile app developers

Industry/Entity Type

Crowdfunding

Requirements
Must have
• Submission forms must have explanation fields next to the form

Homepage should have design in whihc a introductary video can be integrated

```html
<!DOCTYPE html>
<html lang="en">
<head>
<meta charset="utf-8">
<title>Grantly Hub – Crowdfunding Mobile Apps</title>
<link href="https://fonts.googleapis.com/css2?family=Signika:wght@300;400;600&family=Open+Sans:wght@400;600;700&display=swap" rel="stylesheet">
<style>
:root{
  --navy:#0b4a8a;
  --blue:#0f5ea8;
  --blue-light:#2a86cf;
  --cyan:#1fb6e8;
  --green:#9cc416;
  --ink:#222;
  --muted:#666;
  --line:#d9d9d9;
  --red:#e8261f;
  --white:#fff;
  --panel:#dbe4ef;
}
*{box-sizing:border-box;margin:0;padding:0}
h1,h2,h3,h4{font-weight:400}
html,body{width:671px;height:1200px;overflow:hidden;background:var(--white)}
body{font-family:"Open Sans",Arial,sans-serif;color:var(--ink)}
.page{position:relative;width:671px;height:1200px;overflow:hidden}
.abs{position:absolute}

/* header */
.utility-bar{left:387px;top:0;width:198px;height:18px;background:var(--navy);display:flex;align-items:center;padding-left:8px;font-size:6px;color:var(--white);gap:4px;white-space:nowrap}
.utility-bar .login{background:var(--blue-light);padding:2px 4px}
.utility-bar .langs{display:flex;gap:2px;margin-left:4px}
.utility-bar .langs span{width:8px;height:5px;background:#d33}
.utility-bar .langs span:nth-child(2){background:#e63}
.utility-bar .langs span:nth-child(3){background:#eee}
.brand{left:78px;top:14px;display:flex;align-items:center;gap:6px}
.brand-square{width:26px;height:40px;background:var(--blue)}
.brand-name{font-family:"Signika",sans-serif;font-weight:400;font-size:19px;line-height:19px;color:var(--blue)}
.search{left:414px;top:31px;width:131px;height:15px;border:1px solid #ccc;border-radius:2px;font-size:6px;color:#999;padding:3px 5px}
.search svg{position:absolute;right:3px;top:3px}
.social{top:29px;width:16px;height:16px;border-radius:50%;background:var(--blue)}
.nav{left:208px;top:61px;display:flex;font-size:7.5px;color:#555;height:16px;align-items:center;white-space:nowrap}
.nav a{padding:0 11px;color:inherit;text-decoration:none;line-height:16px}
.nav a.active{background:var(--blue);color:var(--white)}

/* hero */
.hero{left:0;top:83px;width:671px;height:278px;background:radial-gradient(ellipse at 55% 20%,#2a7fc8 0%,#0f5ea8 45%,#0a467f 100%)}
.hero-device{left:78px;top:27px;width:142px;height:225px;border-radius:16px;background:linear-gradient(135deg,#f1f1f1 0%,#bdbdbd 60%,#222 61%,#111 100%)}
.hero-title{left:248px;top:22px;font-family:"Signika",sans-serif;font-weight:400;font-size:26px;color:var(--white);white-space:nowrap}
.hero-col{top:78px;color:var(--white);font-family:"Signika",sans-serif}
.hero-col h2{font-weight:400;font-size:19px;margin-bottom:10px}
.hero-col li{list-style:none;font-size:11px;font-weight:300;line-height:19px;display:flex;align-items:center;gap:7px;white-space:nowrap}
.hero-col li::before{content:"";width:7px;height:6px;background:var(--cyan);clip-path:polygon(0 0,70% 0,100% 50%,70% 100%,0 100%)}
.btn{height:20px;font-family:"Signika",sans-serif;font-size:8.5px;color:var(--white);display:flex;align-items:center;justify-content:center;border-radius:2px}
.btn-project{left:264px;top:188px;width:86px;background:linear-gradient(#39c8f2,#11a3d6)}
.btn-funding{left:428px;top:188px;width:90px;background:linear-gradient(#b8dc2a,#86ad0c)}
.ask-tab{left:643px;top:208px;width:28px;height:54px;background:var(--cyan);color:var(--white);font-size:8px;writing-mode:vertical-rl;display:flex;align-items:center;justify-content:center}

/* sections */
.section-title{left:78px;font-family:"Signika",sans-serif;font-weight:400;font-size:12.5px;color:var(--ink)}
.cards{left:78px;display:flex;gap:9px}
.card{position:relative;width:85px;height:70px;background:var(--white);box-shadow:0 0 0 1px #e3e3e3,1px 2px 3px rgba(0,0,0,.15)}
.card-stats{position:absolute;left:0;top:0;width:19px;height:70px;background:var(--navy);color:var(--white);font-size:4.5px;display:flex;flex-direction:column;align-items:center;justify-content:space-around;padding:3px 0}
.card-stats div{display:flex;flex-direction:column;align-items:center;gap:1px}
.card-icon{position:absolute;left:32px;top:10px;width:36px;height:36px;border-radius:6px}
.card-name{position:absolute;left:19px;right:0;top:55px;text-align:center;font-size:6px;color:#333;white-space:nowrap}
.see-all{right:223px;font-size:6px;color:var(--red)}
.divider{left:78px;width:370px;height:2px;background:#e6e6e6}
.store-badge{left:374px;top:790px;width:74px;height:18px;border-radius:3px;background:#e9e9e9}

.ribbon-line{left:78px;width:370px;height:3px;background:#ddd}
.ribbon{left:180px;width:166px;height:20px}
.ribbon span{position:absolute;inset:0;display:flex;align-items:center;justify-content:center;color:var(--white);font-family:"Signika",sans-serif;font-size:11px}
.carousel{left:78px;width:370px;height:36px;display:flex;align-items:center;justify-content:space-between}
.carousel .names{display:flex;gap:30px;align-items:center;font-family:"Signika",sans-serif;font-size:12px;color:#333;font-weight:600;white-space:nowrap}

/* sidebar */
.side-title{left:464px;font-family:"Signika",sans-serif;font-weight:400;font-size:9.5px;color:var(--ink);white-space:nowrap}
.side-title em{font-style:normal;color:var(--red)}
.people{left:464px;display:grid;grid-template-columns:repeat(3,37px);column-gap:7px;row-gap:9px}
.person .photo{width:37px;height:37px;border:1px solid #ddd}
.person p{font-size:5.5px;text-align:center;margin-top:2px;color:#333;white-space:nowrap}
.social-box{left:463px;top:660px;width:127px;height:140px;border:1px solid #ccc;padding:4px;font-size:5px;color:#333}
.social-box .head{display:flex;gap:4px}
.social-box .head .sq{width:18px;height:18px;background:var(--blue);flex:none}
.social-box .head b{color:var(--blue);font-size:6px;display:block;line-height:7px}
.social-box .like{display:inline-block;border:1px solid #999;padding:0 3px;font-size:5px;margin-top:2px;background:#eee}
.social-box .fans{display:grid;grid-template-columns:repeat(5,18px);gap:3px 5px;margin-top:4px}
.social-box .fans div{text-align:center;font-size:3.8px;white-space:nowrap}
.social-box .fans i{display:block;width:18px;height:18px;background:#7a7f8a}
.social-box .foot{position:absolute;bottom:3px;left:4px;font-size:4.5px;color:#555}
.newsletter{left:463px;top:815px;width:127px;height:90px;background:var(--panel);padding:8px 6px}
.newsletter h3{font-family:"Signika",sans-serif;font-weight:600;font-size:10px;color:var(--blue);display:flex;align-items:center;gap:6px}
.newsletter .field{margin-top:9px;height:14px;background:var(--white);border:1px solid #bbb;font-size:5.5px;color:#999;padding:3px 4px}
.newsletter .go{margin-top:6px;width:46px;height:13px;background:var(--navy);color:var(--white);font-size:5.5px;display:flex;align-items:center;justify-content:center}
.video-box{left:463px;top:918px;width:127px;height:112px;border:1px solid #ccc;padding:4px 5px}
.video-box h3{font-family:"Signika",sans-serif;font-weight:400;font-size:8.5px;margin-bottom:3px}
.video-screen{width:116px;height:78px;background:radial-gradient(circle at 50% 45%,#3a3a3a,#050505)}
.video-bar{width:116px;height:11px;background:#e4e4e4;display:flex;align-items:center;gap:4px;padding:0 3px;font-size:4px}

/* footer */
.footer{left:0;top:1094px;width:671px;height:106px;background:var(--navy);color:var(--white);font-size:6.5px}
.footer h4{font-family:"Signika",sans-serif;font-weight:400;font-size:9px;margin-bottom:8px}
.footer p{line-height:12.5px;white-space:nowrap}
.f-sep{top:0;width:1px;height:106px;background:rgba(255,255,255,.2)}
</style>
</head>
<body>
<div class="page">

  <!-- header -->
  <div class="abs utility-bar"><span>Blog</span>|<span>Get AAA Certified</span>|<span>About us</span>|<span class="login">Login</span><span class="langs"><span></span><span></span><span></span></span></div>
  <div class="abs brand"><div class="brand-square"></div><div class="brand-name">Grantly<br>Hub</div></div>
  <div class="abs search">Search here...<svg width="8" height="8" viewBox="0 0 8 8"><circle cx="3.2" cy="3.2" r="2.4" fill="none" stroke="#2a86cf" stroke-width="1"/><line x1="5" y1="5" x2="7.5" y2="7.5" stroke="#2a86cf"/></svg></div>
  <div class="abs social" style="left:553px"></div>
  <div class="abs social" style="left:573px;background:#2f4f6f"></div>
  <nav class="abs nav"><a class="active">Home</a><a>Fund apps</a><a>Submit your app</a><a>Find a developer</a><a>How it works</a><a>Register</a></nav>

  <!-- hero -->
  <section class="abs hero">
    <div class="abs hero-device" role="img" aria-label="Two smartphones showing a mobile app splash screen"></div>
    <h1 class="abs hero-title">Crowdfunding Mobile Apps</h1>
    <div class="abs hero-col" style="left:249px"><h2>App Builders :</h2><ul><li>Fund Your Development</li><li>Get Downloads</li><li>Keep 100% Qwenrship</li></ul></div>
    <div class="abs hero-col" style="left:413px"><h2>Funders :</h2><ul><li>Get Great Returns on Your Funding</li><li>Fund Per Milestone</li><li>Be Part of A Succes Story</li></ul></div>
    <div class="abs btn btn-project">START PROJECT</div>
    <div class="abs btn btn-funding">START FUNDING</div>
  </section>
  <div class="abs ask-tab">Ask Us</div>

  <!-- Most funded -->
  <h2 class="abs section-title" style="top:371px">Most Funded Apps</h2>
  <div class="abs cards" style="top:399px">
    <div class="card"><div class="card-stats"><div><svg width="6" height="5" viewBox="0 0 6 5"><path d="M3 5L0.4 2.3A1.4 1.4 0 0 1 3 1a1.4 1.4 0 0 1 2.6 1.3z" fill="#fff"/></svg>(11)</div><div><svg width="5" height="5"><circle cx="2.5" cy="2.5" r="2.3" fill="#fff"/></svg>(60)</div><div><svg width="6" height="5"><rect width="6" height="4" rx="1" fill="#fff"/></svg>(253)</div></div><div class="card-icon" role="img" aria-label="App icon: chalkboard drawing game" style="background:#3b3328"></div><div class="card-name">Sketch Riddler</div></div>
    <div class="card"><div class="card-stats"><div><svg width="6" height="5" viewBox="0 0 6 5"><path d="M3 5L0.4 2.3A1.4 1.4 0 0 1 3 1a1.4 1.4 0 0 1 2.6 1.3z" fill="#fff"/></svg>(11)</div><div><svg width="5" height="5"><circle cx="2.5" cy="2.5" r="2.3" fill="#fff"/></svg>(60)</div><div><svg width="6" height="5"><rect width="6" height="4" rx="1" fill="#fff"/></svg>(253)</div></div><div class="card-icon" role="img" aria-label="App icon: city travel guide" style="background:linear-gradient(#8fd0f0,#e89a6a)"></div><div class="card-name">Mia's City Tr...</div></div>
    <div class="card"><div class="card-stats"><div><svg width="6" height="5" viewBox="0 0 6 5"><path d="M3 5L0.4 2.3A1.4 1.4 0 0 1 3 1a1.4 1.4 0 0 1 2.6 1.3z" fill="#fff"/></svg>(11)</div><div><svg width="5" height="5"><circle cx="2.5" cy="2.5" r="2.3" fill="#fff"/></svg>(60)</div><div><svg width="6" height="5"><rect width="6" height="4" rx="1" fill="#fff"/></svg>(253)</div></div><div class="card-icon" role="img" aria-label="App icon: pattern puzzle mascot" style="background:#c8202a"></div><div class="card-name">TileTiger</div></div>
    <div class="card"><div class="card-stats"><div><svg width="6" height="5" viewBox="0 0 6 5"><path d="M3 5L0.4 2.3A1.4 1.4 0 0 1 3 1a1.4 1.4 0 0 1 2.6 1.3z" fill="#fff"/></svg>(11)</div><div><svg width="5" height="5"><circle cx="2.5" cy="2.5" r="2.3" fill="#fff"/></svg>(60)</div><div><svg width="6" height="5"><rect width="6" height="4" rx="1" fill="#fff"/></svg>(253)</div></div><div class="card-icon" role="img" aria-label="App icon: orange letter tile" style="background:linear-gradient(#f29a2e,#d86b10)"></div><div class="card-name">Zoomibo</div></div>
  </div>
  <div class="abs see-all" style="top:481px">See all &gt;&gt;</div>
  <div class="abs divider" style="top:505px"></div>

  <!-- Staff picks -->
  <h2 class="abs section-title" style="top:518px">Our Staff's Picks</h2>
  <div class="abs cards" style="top:545px">
    <div class="card"><div class="card-stats"><div><svg width="6" height="5" viewBox="0 0 6 5"><path d="M3 5L0.4 2.3A1.4 1.4 0 0 1 3 1a1.4 1.4 0 0 1 2.6 1.3z" fill="#fff"/></svg>(11)</div><div><svg width="5" height="5"><circle cx="2.5" cy="2.5" r="2.3" fill="#fff"/></svg>(60)</div><div><svg width="6" height="5"><rect width="6" height="4" rx="1" fill="#fff"/></svg>(253)</div></div><div class="card-icon" role="img" aria-label="App icon: health cross" style="background:#f2c9cd"></div><div class="card-name">My VitalBuddy</div></div>
    <div class="card"><div class="card-stats"><div><svg width="6" height="5" viewBox="0 0 6 5"><path d="M3 5L0.4 2.3A1.4 1.4 0 0 1 3 1a1.4 1.4 0 0 1 2.6 1.3z" fill="#fff"/></svg>(11)</div><div><svg width="5" height="5"><circle cx="2.5" cy="2.5" r="2.3" fill="#fff"/></svg>(60)</div><div><svg width="6" height="5"><rect width="6" height="4" rx="1" fill="#fff"/></svg>(253)</div></div><div class="card-icon" role="img" aria-label="App icon: pink coupon box" style="background:#d9388a"></div><div class="card-name">Dealpocket</div></div>
    <div class="card"><div class="card-stats"><div><svg width="6" height="5" viewBox="0 0 6 5"><path d="M3 5L0.4 2.3A1.4 1.4 0 0 1 3 1a1.4 1.4 0 0 1 2.6 1.3z" fill="#fff"/></svg>(11)</div><div><svg width="5" height="5"><circle cx="2.5" cy="2.5" r="2.3" fill="#fff"/></svg>(60)</div><div><svg width="6" height="5"><rect width="6" height="4" rx="1" fill="#fff"/></svg>(253)</div></div><div class="card-icon" role="img" aria-label="App icon: football quiz helmet" style="background:#8a7a66"></div><div class="card-name">Gridiron Quiz...</div></div>
    <div class="card"><div class="card-stats"><div><svg width="6" height="5" viewBox="0 0 6 5"><path d="M3 5L0.4 2.3A1.4 1.4 0 0 1 3 1a1.4 1.4 0 0 1 2.6 1.3z" fill="#fff"/></svg>(11)</div><div><svg width="5" height="5"><circle cx="2.5" cy="2.5" r="2.3" fill="#fff"/></svg>(60)</div><div><svg width="6" height="5"><rect width="6" height="4" rx="1" fill="#fff"/></svg>(253)</div></div><div class="card-icon" role="img" aria-label="App icon: cartoon game character" style="background:#e0b25a"></div><div class="card-name">Pirro Master...</div></div>
  </div>
  <div class="abs see-all" style="top:626px">See all &gt;&gt;</div>
  <div class="abs divider" style="top:647px"></div>

  <!-- Successfully funded -->
  <h2 class="abs section-title" style="top:663px">Successfully Funded</h2>
  <div class="abs cards" style="top:690px">
    <div class="card"><div class="card-stats"><div><svg width="6" height="5" viewBox="0 0 6 5"><path d="M3 5L0.4 2.3A1.4 1.4 0 0 1 3 1a1.4 1.4 0 0 1 2.6 1.3z" fill="#fff"/></svg>(11)</div><div><svg width="5" height="5"><circle cx="2.5" cy="2.5" r="2.3" fill="#fff"/></svg>(60)</div><div><svg width="6" height="5"><rect width="6" height="4" rx="1" fill="#fff"/></svg>(253)</div></div><div class="card-icon" role="img" aria-label="App icon: pixel strategy warrior" style="background:#4f7a2e"></div><div class="card-name">Stratos: Anci...</div></div>
    <div class="card"><div class="card-stats"><div><svg width="6" height="5" viewBox="0 0 6 5"><path d="M3 5L0.4 2.3A1.4 1.4 0 0 1 3 1a1.4 1.4 0 0 1 2.6 1.3z" fill="#fff"/></svg>(11)</div><div><svg width="5" height="5"><circle cx="2.5" cy="2.5" r="2.3" fill="#fff"/></svg>(60)</div><div><svg width="6" height="5"><rect width="6" height="4" rx="1" fill="#fff"/></svg>(253)</div></div><div class="card-icon" role="img" aria-label="App icon: monochrome telecom emblem" style="background:#e9e9e9"></div><div class="card-name">Mobile Norse...</div></div>
    <div class="card"><div class="card-stats"><div><svg width="6" height="5" viewBox="0 0 6 5"><path d="M3 5L0.4 2.3A1.4 1.4 0 0 1 3 1a1.4 1.4 0 0 1 2.6 1.3z" fill="#fff"/></svg>(11)</div><div><svg width="5" height="5"><circle cx="2.5" cy="2.5" r="2.3" fill="#fff"/></svg>(60)</div><div><svg width="6" height="5"><rect width="6" height="4" rx="1" fill="#fff"/></svg>(253)</div></div><div class="card-icon" role="img" aria-label="App icon: thermometer alert" style="background:linear-gradient(#f3f3f3,#d6d6d6)"></div><div class="card-name">QuickPing</div></div>
    <div class="card"><div class="card-stats"><div><svg width="6" height="5" viewBox="0 0 6 5"><path d="M3 5L0.4 2.3A1.4 1.4 0 0 1 3 1a1.4 1.4 0 0 1 2.6 1.3z" fill="#fff"/></svg>(11)</div><div><svg width="5" height="5"><circle cx="2.5" cy="2.5" r="2.3" fill="#fff"/></svg>(60)</div><div><svg width="6" height="5"><rect width="6" height="4" rx="1" fill="#fff"/></svg>(253)</div></div><div class="card-icon" role="img" aria-label="App icon: dark sheet music folder" style="background:#2c2c2c"></div><div class="card-name">Score Reader...</div></div>
  </div>
  <div class="abs see-all" style="top:771px">See all &gt;&gt;</div>
  <div class="abs store-badge"></div>

  <!-- Featured on -->
  <div class="abs ribbon-line" style="top:852px"></div>
  <div class="abs ribbon" style="top:843px"><svg width="166" height="20" viewBox="0 0 166 20"><polygon points="0,0 166,0 158,10 166,20 0,20 8,10" fill="#0f5ea8"/></svg><span>Featured on</span></div>
  <div class="abs carousel" style="top:886px">
    <svg width="18" height="36" viewBox="0 0 18 36"><polyline points="17,1 1,18 17,35" fill="none" stroke="#ccc"/></svg>
    <div class="names"><span>The Capital Ledger</span><span>StartPulse</span><span style="font-weight:400">DealIndex</span></div>
    <svg width="18" height="36" viewBox="0 0 18 36"><polyline points="1,1 17,18 1,35" fill="none" stroke="#ccc"/></svg>
  </div>

  <!-- Partners -->
  <div class="abs ribbon-line" style="top:968px"></div>
  <div class="abs ribbon" style="top:959px"><svg width="166" height="20" viewBox="0 0 166 20"><polygon points="0,0 166,0 158,10 166,20 0,20 8,10" fill="#0f5ea8"/></svg><span>Partners</span></div>
  <div class="abs carousel" style="top:1008px">
    <svg width="18" height="36" viewBox="0 0 18 36"><polyline points="17,1 1,18 17,35" fill="none" stroke="#ccc"/></svg>
    <div class="names" style="gap:44px;font-size:14px"><span>Movora</span><span>Kelvix</span><span>Lumenlab</span></div>
    <svg width="18" height="36" viewBox="0 0 18 36"><polyline points="1,1 17,18 1,35" fill="none" stroke="#ccc"/></svg>
  </div>

  <!-- sidebar -->
  <h3 class="abs side-title" style="top:371px">Most Active Funders</h3>
  <div class="abs people" style="top:395px">
    <div class="person"><div class="photo" role="img" aria-label="Funder profile photo" style="background:#2d3f8f"></div><p>Tam</p></div>
    <div class="person"><div class="photo" role="img" aria-label="Default member avatar" style="background:#cdd5e3"></div><p>Vu</p></div>
    <div class="person"><div class="photo" role="img" aria-label="Funder profile graphic" style="background:#7a5a3a"></div><p>Ruud Ve</p></div>
    <div class="person"><div class="photo" role="img" aria-label="Funder profile photo" style="background:#b88c6a"></div><p>Pieter K...</p></div>
    <div class="person"><div class="photo" role="img" aria-label="Funder profile photo" style="background:#6b7a4e"></div><p>Olaf</p></div>
    <div class="person"><div class="photo" role="img" aria-label="Funder profile photo" style="background:#1f2a44"></div><p>Ray Mun...</p></div>
  </div>

  <h3 class="abs side-title" style="top:517px">New Members <em>Just Signed Up</em></h3>
  <div class="abs people" style="top:543px">
    <div class="person"><div class="photo" role="img" aria-label="Member profile photo" style="background:#3a5a8a"></div><p>Wade P...</p></div>
    <div class="person"><div class="photo" role="img" aria-label="Default member avatar" style="background:#cdd5e3"></div><p>KRT Mob...</p></div>
    <div class="person"><div class="photo" role="img" aria-label="Member profile photo" style="background:#9a8a7a"></div><p>Lina S...</p></div>
    <div class="person"><div class="photo" role="img" aria-label="Member avatar graphic" style="background:#eeeeee"></div><p>Milo</p></div>
    <div class="person"><div class="photo" role="img" aria-label="Member avatar graphic" style="background:#e89a1a"></div><p>devrazaq</p></div>
    <div class="person"><div class="photo" role="img" aria-label="Default member avatar" style="background:#cdd5e3"></div><p>test</p></div>
  </div>

  <div class="abs social-box">
    <div class="head"><div class="sq"></div><div><b>GrantlyHub - Crowdfunding Mobile Apps</b> on Chatterly<br><span class="like">Like</span></div></div>
    <p style="margin-top:4px">3,443 people like <b>GrantlyHub - Crowdfunding Mobile Apps.</b></p>
    <div class="fans">
      <div><i role="img" aria-label="Fan photo"></i>Ravindra</div><div><i role="img" aria-label="Fan photo"></i>JQ</div><div><i role="img" aria-label="Fan photo"></i>Nadia</div><div><i role="img" aria-label="Fan photo"></i>Omar</div><div></div>
      <div><i role="img" aria-label="Fan photo"></i>Priyank</div><div><i role="img" aria-label="Fan photo"></i>Tomas</div><div><i role="img" aria-label="Fan photo"></i>Lenka</div><div><i role="img" aria-label="Fan photo"></i>Kb</div><div></div>
    </div>
    <div class="foot">Chatterly social plugin</div>
  </div>

  <div class="abs newsletter">
    <h3><svg width="22" height="16" viewBox="0 0 22 16"><rect x="1" y="1" width="20" height="14" fill="#0f5ea8"/><polyline points="1,1 11,9 21,1" fill="none" stroke="#fff" stroke-width="1.2"/></svg>Our Newsletter!</h3>
    <div class="field">Enter Your Email...</div>
    <div class="go">SUBSCRIBE</div>
  </div>

  <div class="abs video-box">
    <h3>How to Work</h3>
    <div class="video-screen" role="img" aria-label="Introductory video poster" style="display:flex;align-items:center;justify-content:center">
      <svg width="26" height="26" viewBox="0 0 26 26"><circle cx="13" cy="13" r="12" fill="rgba(255,255,255,.25)" stroke="#fff" stroke-width="1.5"/><polygon points="10,7 19,13 10,19" fill="#fff"/></svg>
    </div>
    <div class="video-bar"><svg width="5" height="5"><polygon points="0,0 5,2.5 0,5" fill="#333"/></svg><span style="flex:1;height:2px;background:#aaa"></span><span>0:00 / 0:00</span></div>
  </div>

  <!-- footer -->
  <footer class="abs footer">
    <div class="abs" style="left:79px;top:14px"><h4>Contact Us</h4><p>GrantlyHub Ltd.<br>214 Harbour Lane<br>Westbay, Northgate<br>Port Alder</p></div>
    <div class="abs" style="left:172px;top:37px;display:flex;gap:5px">
      <div style="display:flex;flex-direction:column;gap:14px;padding-top:2px">
        <svg width="8" height="8" viewBox="0 0 8 8"><path d="M1 1h2l1 2-1 1a4 4 0 0 0 2 2l1-1 2 1v2c-4 0-7-3-7-7z" fill="#fff"/></svg>
        <svg width="8" height="6" viewBox="0 0 8 6"><rect width="8" height="6" fill="#fff"/><polyline points="0,0 4,3 8,0" fill="none" stroke="#0b4a8a"/></svg>
      </div>
      <p>Phone :<br>555 210 4477<br>Email :<br>hello@ grantlyhub.com</p>
    </div>
    <div class="abs f-sep" style="left:275px"></div>
    <div class="abs" style="left:298px;top:14px"><h4>Quick Links</h4><p>Home<br>Fund apps<br>Submit your app<br>Find a developer</p></div>
    <div class="abs" style="left:397px;top:31px"><p>How it works<br>Register<br>Blog<br>Contact Us</p></div>
    <div class="abs f-sep" style="left:453px"></div>
    <div class="abs" style="left:515px;top:26px;width:14px;height:26px;border:1.5px solid #fff;border-radius:2px"></div>
    <div class="abs" style="left:472px;top:76px;white-space:nowrap">©2012 Grantly Hub. All Rights Reserved.</div>
  </footer>

</div>
</body>
</html>
```